Business card design based on existing website

Please make a business card that is consistent with the look and feel of my new website: http://brindleworth.com.sg. By going to the site, I think you'll have all you need in terms of the work I do and the colors I use.

I would like to ask the winner of this project to then do a separate project to design my stationery.

Target Market(s)

Heads of human resources, people wanting psychotherapy, and executives wanting coaching. (It's quite a mix!)

Industry/Entity Type

Psychology

Contact Information for Business Card

Email: pax5678@brindleworth.com.sg
Website: http://brindleworth.com.sg
Tel: +65 94706152

(I will not have a physical address on the card)

Font styles to use
Serif

Colors

Designer to choose colors to be used in the design.

Requirements
Must have
• On the Front
• ==========
• Have "Dr. Everett Brindleworth" using the font of the website.
• Also "Executive Coach, Psychotherapist, Leadership Professor"
• The back should mention
• ==================
• My degrees
• -------------
• "PhD Kelvale; Post Doc Duncliffe". E.g., "Everett Brindleworth (PhD Kelvale; Post Doc Duncliffe)" where the text between brackets was in smaller font.
• My work
• ----------
• "Executive coach, psychotherapist, and leadership professor"
• My job titles
• ---------------
• "Principal (Brindleworth Consulting)
• Adjunct Professor (Orchid Crest University)
• Adjunct Associate Professor (Meridian Strait University)
• Coach & Supervisor (VORELT) '
• Options:
• 1) you can abbreviate Adjunct Professor to "Adj Prof" or "Adj Professor"; and "Adjunct Associate Professor" to "Adj Assoc Prof"
• 2) you abbreviate "Meridian Strait University" and "Orchid Crest University" to "MSU" and "OCU"
• 3) You can also combine the titles for MSU and OCU, e.g., "Adjunct faculty (MSU & OCU)
Nice to have
• Because I work with many Chinese people, it is sometimes helpful to have my family name, "Brindleworth", in caps. In the past I have not used caps because it takes away from the aesthetic of the card. Only use caps if it looks good.
• The uploaded image of a "EB" is something that may be helpful. I am undecided.
• THANK YOU for helping me!
Should not have
• No photos. In my industry people consider it overselling.

```html
<!DOCTYPE html>
<html lang="en">
<head>
<meta charset="utf-8">
<title>Dr. Everett Brindleworth – Business Card</title>
<link rel="stylesheet" href="https://fonts.googleapis.com/css2?family=PT+Serif:wght@400;700&display=swap">
<style>
  :root {
    --forest: #1c4600;
    --lime: #86fc5a;
    --ink: #0e0e0e;
    --text-dark: #141414;
    --accent: #7ef52a;
  }
  * { margin: 0; padding: 0; box-sizing: border-box; }
  html, body {
    width: 1200px;
    height: 720px;
    overflow: hidden;
    background: var(--forest);
  }
  .card {
    position: relative;
    width: 1200px;
    height: 720px;
    background: var(--forest);
    font-family: "PT Serif", Georgia, serif;
  }
  .identity-band {
    position: absolute;
    left: 0;
    top: 222px;
    width: 945px;
    height: 276px;
    background: var(--lime);
  }
  .identity {
    position: absolute;
    right: 62px;
    top: 84px;
    text-align: right;
  }
  .identity__name {
    font-size: 42px;
    font-weight: 400;
    line-height: 1.1;
    color: var(--forest);
  }
  .identity__surname { font-weight: 700; }
  .identity__tagline {
    margin-top: 4px;
    font-size: 30px;
    line-height: 1.2;
    color: var(--text-dark);
  }
  .monogram-panel {
    position: absolute;
    left: 945px;
    top: 222px;
    width: 255px;
    height: 276px;
    background: var(--ink);
    display: flex;
    align-items: center;
    justify-content: center;
  }
  .monogram {
    font-size: 84px;
    font-weight: 400;
    letter-spacing: 2px;
    color: var(--accent);
    line-height: 1;
  }
</style>
</head>
<body>
  <main class="card">
    <section class="identity-band">
      <div class="identity">
        <h1 class="identity__name">Dr. Everett <span class="identity__surname">BRINDLEWORTH</span></h1>
        <p class="identity__tagline">Advancing Human Development</p>
      </div>
    </section>
    <aside class="monogram-panel">
      <span class="monogram">EB</span>
    </aside>
  </main>
</body>
</html>
```